2026 Compostable Stand up Pouch Redesign

Project Overview
We are a natural dog bakery focused on simple, healthy ingredients and earth-friendly packaging. As the first step in a rebrand, we are redesigning our 6 oz stand-up pouch using new compostable packaging materials.
New pouch is the same size and structure as current (template provided)
Files included:
Existing Art template (PDF + JPG)
Photos of current packaging (for reference only)
Copy of existing logo (Meadowtail Provisions Bakery)
Copy of future logo (Birchwood Hound Natural Bakery)
This redesign should feel like a clear upgrade—more refined, more intentional, and more aligned with sustainability.
⚠️ IMPORTANT LAYOUT CONSTRAINT (PLEASE READ)
The new pouch has a full-width horizontal window.
Design elements may ONLY appear above and below the window
No design elements can be placed to the left or right of the window
A 4.5" W x 3.5" H blank space above the window must be preserved
This is reserved for applied product labels
Keep this area completely clean (no textures, patterns, or graphics)
Submissions that ignore these elements will not be considered.
Brand Direction & Style
We are looking for a design that feels:
Natural and ingredient-focused
Eco-conscious and sustainable
Clean and elevated (not rustic, not overly playful)
Warm and trustworthy
Avoid:
Neon or bright artificial colors
Loud, busy, or overly commercial designs
Cartoon-heavy or overly whimsical styles
Color Direction
Our current packaging is kraft brown, but the new material allows full-color printing. We are looking for:
Nature-inspired colors only
Greens, muted blues, warm browns, soft earth tones
Background color is flexible within this palette
Must work with:
Current logo: Meadowtail Provisions Bakery
Future logo: Birchwood Hound Natural Bakery
👉 For this project, use Meadowtail Provisions Bakery logo only
Front of Pouch Requirements
Do NOT include logo on pouch front
(Logo will be on applied labels)
Required Elements
Tagline: Simple, Healthy Ingredients. Earth Friendly Packaging.
Compostable Messaging (REQUIRED):
Must clearly communicate that packaging is compostable
Optional placement:
Tear-off strip near hang hole
BUT must also appear somewhere on the main pouch design
Origin Callout:
“Hand Made in the Pacific Northwest”
Can be a badge, stamp, or graphic (open to redesign)
Icons (Highly Encouraged)
We would like to explore a clean, minimal icon set for:
No Corn
No Wheat
No Soy
No GMOs
Compostable Packaging
(Keep icons simple, clean, and consistent with natural aesthetic)
Back of Pouch Requirements
Messaging Direction
Do NOT use: “The healthiest pet bakery in the US”
Instead, build around:
Simple, Healthy Ingredients. Earth Friendly Packaging.
Content
“Our Recipes” bullet points (from current packaging – still valid)
Sustainability messaging:
Include reference to reducing our “carbon pawprint”
Emphasize eco-friendly materials and practices
Design Direction
Open to new layout and graphics
Should visually reinforce:
Clean ingredients
Natural sourcing
Sustainability
Printing Considerations
Design should be mindful of production scalability:
Should translate well to both digital and roto printing
Avoid overly complex gradients or excessive color layering
Creative Freedom (Important)
While we have outlined structure and constraints, we are intentionally leaving visual interpretation open.
We welcome:
Fresh layout ideas
Refined graphic elements
Elevated visual storytelling
We are especially interested in designs that feel:
Thoughtful
Clean
Naturally premium
Any design submission that includes loud, neon, or "aggressive" color schemes or a mass market appeal will be eliminated immediately. We are a premium, natural dog bakery found in independent stores only.
UPDATED & IMPORTANT DESIGN REQUIREMENTS (PLEASE READ)
This pouch is a base design used across all flavors. A separate product label will be applied.
A clearly defined blank area must be left for label placement (do not incorporate into artwork).
The product viewing window is fixed:
Size and placement must match the template exactly
Do not resize, reposition, or redesign the window
Designs that do not follow these requirements will not be considered.
Please review the discussion board for additional feedback and direction before submitting revisions.

```html
<!DOCTYPE html>
<html lang="en">
<head>
<meta charset="utf-8">
<title>Compostable Stand-up Pouch – Front and Back</title>
<link rel="stylesheet" href="https://fonts.googleapis.com/css2?family=Staatliches&family=Fraunces:wght@600&family=Baloo+2:wght@500;600&display=swap">
<style>
  :root {
    --backdrop: #8bb04a;
    --leaf: #5e7f33;
    --leaf-dark: #4b6a27;
    --leaf-deep: #2f5a2a;
    --cream: #efe5cf;
    --cream-light: #f5eedd;
    --bark: #4a3020;
    --ink: #3a3226;
    --olive-text: #4f5a2a;
    --white: #ffffff;
  }
  * { margin: 0; padding: 0; box-sizing: border-box; }
  html, body { width: 1200px; height: 945px; overflow: hidden; }
  body {
    background: var(--backdrop);
    font-family: "Baloo 2", sans-serif;
    position: relative;
  }
  .pouch {
    position: absolute;
    top: 152px;
    width: 460px;
    height: 606px;
    background: var(--cream);
    border-radius: 4px 4px 16px 16px;
    overflow: hidden;
  }
  .pouch--front { left: 128px; }
  .pouch--back { left: 641px; }

  .tear-strip {
    position: absolute; left: 0; top: 0; width: 100%; height: 56px;
    background: var(--leaf);
  }
  .tear-strip__line {
    position: absolute; left: 0; right: 0; top: 31px;
    border-top: 1px dashed rgba(255,255,255,0.55);
  }
  .tear-strip__text {
    position: absolute; left: 50%; top: 22px; transform: translateX(-50%);
    background: var(--leaf); padding: 0 8px;
    color: var(--cream-light); font-size: 12px; line-height: 18px; white-space: nowrap;
    font-weight: 500;
  }
  .tear-strip__text strong { font-weight: 600; }

  .label-area {
    position: absolute; left: 80px; top: 78px; width: 300px; height: 180px;
    background: var(--cream);
  }

  .photo { position: absolute; }
  .photo--window {
    left: 18px; top: 270px; width: 424px; height: 150px;
    background: linear-gradient(180deg, #7c5a38 0%, #a07a52 50%, #86623e 100%);
    clip-path: polygon(0 14%, 100% 0, 100% 88%, 0 100%);
  }
  .photo--meadow {
    left: 0; top: 536px; width: 100%; height: 70px;
    background: linear-gradient(180deg, #9cc455 0%, #6fa53a 60%, #5a8f2e 100%);
    clip-path: polygon(0 30%, 40% 10%, 100% 0, 100% 100%, 0 100%);
  }
  .photo--bowl {
    left: 0; top: 258px; width: 104px; height: 210px;
    background: radial-gradient(circle at 0% 50%, #e2b04a 0%, #d6a43e 60%, #f2efe8 72%, rgba(242,239,232,0) 78%);
  }
  .photo--running-dog {
    left: 312px; top: 240px; width: 135px; height: 250px;
    background: radial-gradient(ellipse at 55% 45%, #c9b38e 0%, #ddd0b4 50%, rgba(239,229,207,0) 75%);
  }

  .seal {
    position: absolute; border-radius: 50%;
    background: var(--leaf-deep); border: 4px solid var(--leaf);
    box-shadow: 0 0 0 3px var(--cream-light);
  }
  .seal--front { left: 323px; top: 228px; width: 80px; height: 80px; }
  .seal--back { left: 199px; top: 154px; width: 76px; height: 76px; }

  .ribbon {
    position: absolute; left: 92px; top: 398px; width: 276px; height: 86px;
    background: linear-gradient(180deg, #7ea43d, #5e8630);
    clip-path: polygon(0 6%, 50% 0, 100% 6%, 100% 100%, 50% 94%, 0 100%);
    text-align: center;
  }
  .ribbon__script {
    font-family: "Fraunces", serif; font-weight: 600; font-size: 18px;
    color: var(--leaf-dark); margin-top: 5px; line-height: 22px;
    background: var(--cream-light); display: inline-block; padding: 0 8px; border-radius: 3px;
  }
  .ribbon__title {
    font-family: "Staatliches", sans-serif; font-size: 32px; line-height: 34px;
    color: var(--white); letter-spacing: 1px;
  }
  .ribbon__tagline {
    font-size: 10px; font-weight: 600; line-height: 12px;
    color: var(--cream-light); letter-spacing: 0.6px;
  }

  .free-from {
    position: absolute; left: 30px; top: 490px; width: 400px;
    display: flex; justify-content: space-between; padding: 0 20px;
  }
  .free-from__item { text-align: center; width: 70px; }
  .free-from__item svg { width: 40px; height: 40px; }
  .free-from__label { font-size: 12px; color: var(--ink); font-weight: 500; line-height: 14px; }

  .origin-stamp {
    position: absolute; left: 178px; top: 566px; width: 104px; height: 32px;
    background: var(--cream-light); border: 1.5px solid var(--ink); border-radius: 6px;
    font-family: "Fraunces", serif; font-size: 8.5px; line-height: 10px;
    color: var(--ink); text-align: center; padding-top: 5px;
  }

  .headline {
    position: absolute; left: 0; width: 100%; text-align: center;
  }
  .headline--simple {
    top: 72px; font-family: "Staatliches", sans-serif; font-size: 58px; line-height: 54px;
    color: var(--bark); letter-spacing: 1px; font-weight: 400;
  }
  .headline--sub {
    top: 126px; font-size: 12px; font-weight: 600; color: var(--bark); letter-spacing: 0.3px;
  }

  .feature-list { position: absolute; }
  .feature-list--recipes { left: 122px; top: 246px; }
  .feature-list--commitment { left: 128px; top: 356px; }
  .feature-list__title {
    font-family: "Staatliches", sans-serif; font-size: 14px; color: var(--ink);
    letter-spacing: 0.5px; margin-bottom: 4px; font-weight: 400;
  }
  .feature-list__item {
    display: flex; align-items: center; gap: 8px;
    font-size: 10px; font-weight: 500; color: var(--olive-text); height: 20px;
  }
  .feature-list__dot {
    width: 14px; height: 14px; border-radius: 50%; background: #d6e2b0;
    border: 1px solid #9cb860;
  }
  .divider {
    position: absolute; left: 132px; top: 342px; width: 202px;
    border-top: 1px dashed #8c8070;
  }

  .footer-band {
    position: absolute; left: 0; bottom: 0; width: 100%; height: 150px;
    background: var(--leaf);
    clip-path: polygon(0 8%, 30% 4%, 60% 6%, 100% 0, 100% 100%, 0 100%);
  }
  .footer-band__title {
    position: absolute; left: 0; width: 100%; top: 34px; text-align: center;
    font-family: "Staatliches", sans-serif; font-size: 22px; color: var(--white); letter-spacing: 1px;
  }
  .footer-band__sub {
    position: absolute; left: 0; width: 100%; top: 60px; text-align: center;
    font-size: 11px; font-weight: 500; color: var(--cream-light);
  }
  .cert-row {
    position: absolute; left: 0; width: 100%; top: 96px;
    display: flex; justify-content: center; gap: 40px;
  }
  .cert { width: 40px; height: 40px; border: 2px solid var(--cream-light); }
  .cert--round { border-radius: 50%; }
  .cert--square { border-radius: 4px; }
</style>
</head>
<body>

<section class="pouch pouch--front">
  <div class="tear-strip">
    <div class="tear-strip__line"></div>
    <div class="tear-strip__text">Tear Here &nbsp;•&nbsp; <strong>100% COMPOSTABLE</strong> &nbsp;•</div>
  </div>

  <div class="label-area" aria-label="Blank area reserved for product label"></div>

  <div class="photo photo--window" role="img" aria-label="Clear product window showing round baked dog treats"></div>
  <div class="seal seal--front" role="img" aria-label="Eco-friendly packaging seal"></div>

  <div class="ribbon">
    <div class="ribbon__script">Simple, Healthy</div>
    <div class="ribbon__title">INGREDIENTS</div>
    <div class="ribbon__tagline">EARTH FRIENDLY PACKAGING</div>
  </div>

  <div class="photo photo--meadow" role="img" aria-label="Green meadow with pine trees"></div>

  <div class="free-from">
    <div class="free-from__item">
      <svg viewBox="0 0 44 44"><circle cx="22" cy="22" r="19" fill="none" stroke="#6b3f2a" stroke-width="2.4"/><line x1="9" y1="9" x2="35" y2="35" stroke="#6b3f2a" stroke-width="2.4"/></svg>
      <div class="free-from__label">No Corn</div>
    </div>
    <div class="free-from__item">
      <svg viewBox="0 0 44 44"><circle cx="22" cy="22" r="19" fill="none" stroke="#6b3f2a" stroke-width="2.4"/><line x1="9" y1="9" x2="35" y2="35" stroke="#6b3f2a" stroke-width="2.4"/></svg>
      <div class="free-from__label">No Wheat</div>
    </div>
    <div class="free-from__item">
      <svg viewBox="0 0 44 44"><circle cx="22" cy="22" r="19" fill="none" stroke="#6b3f2a" stroke-width="2.4"/><line x1="9" y1="9" x2="35" y2="35" stroke="#6b3f2a" stroke-width="2.4"/></svg>
      <div class="free-from__label">No Soy</div>
    </div>
    <div class="free-from__item">
      <svg viewBox="0 0 44 44"><circle cx="22" cy="22" r="19" fill="none" stroke="#6b3f2a" stroke-width="2.4"/><line x1="9" y1="9" x2="35" y2="35" stroke="#6b3f2a" stroke-width="2.4"/></svg>
      <div class="free-from__label">No Gmos</div>
    </div>
  </div>

  <div class="origin-stamp">Hand Made in<br>Pacific Northwest</div>
</section>

<section class="pouch pouch--back">
  <div class="tear-strip">
    <div class="tear-strip__line"></div>
    <div class="tear-strip__text">Tear Here &nbsp;•&nbsp; <strong>100% COMPOSTABLE</strong> &nbsp;•</div>
  </div>

  <h1 class="headline headline--simple">SIMPLE</h1>
  <p class="headline headline--sub">HEALTHY INGREDIENTS. EARTH FRIENDLY PACKAGING.</p>
  <div class="seal seal--back" role="img" aria-label="Eco-friendly packaging seal"></div>

  <div class="photo photo--bowl" role="img" aria-label="White bowl of bone-shaped baked treats"></div>
  <div class="photo photo--running-dog" role="img" aria-label="Photo of a yellow labrador running"></div>

  <div class="feature-list feature-list--recipes">
    <h2 class="feature-list__title">OUR RECIPES:</h2>
    <div class="feature-list__item"><span class="feature-list__dot"></span>Limited Ingredients</div>
    <div class="feature-list__item"><span class="feature-list__dot"></span>All Natural &amp; Delicious</div>
    <div class="feature-list__item"><span class="feature-list__dot"></span>Oven-Baked in Small Batches</div>
  </div>

  <div class="divider"></div>

  <div class="feature-list feature-list--commitment">
    <h2 class="feature-list__title">OUR COMMITMENT:</h2>
    <div class="feature-list__item"><span class="feature-list__dot"></span>Reducing Our Carbon Pawprint</div>
    <div class="feature-list__item"><span class="feature-list__dot"></span>Compostable &amp; Eco-Friendly Materials</div>
    <div class="feature-list__item"><span class="feature-list__dot"></span>Sustainable Practices</div>
  </div>

  <div class="footer-band">
    <div class="footer-band__title">CRAFTED WITH LOVE</div>
    <div class="footer-band__sub">IN THE PACIFIC NORTHWEST</div>
    <div class="cert-row">
      <span class="cert cert--round"></span>
      <span class="cert cert--square"></span>
      <span class="cert cert--round"></span>
    </div>
  </div>
</section>

</body>
</html>
```